Managed Service Provider VOIP Flyer

Looking for a one page US letter size single or double sided brochure to offer cloud hosted VoIP Phone system and unified communications. We have partnered with a VoIP Phone system company and want to sell their services but we don't want their name to be shown on the brochure because customers might call them directly. The company name is Quorvel (www.quorvel-example.com) and our company name is Lumen By Harlow, LLC and our voice product is called Clearly Talk. I have also uploaded my company's logo that you should show on the brochure and use that coloring. For more details about the product, you can visit their website mentioned above. Also I am looking for something very similar to this project and many of the technical details are the same https://flyer.contestpad-example.com/contest/5817264

I have also uploaded a PDF with my different package levels and some of the included features. Depending on the design we may or may not want the package levels on this flyer.

Target Market(s)

Small and medium Businesses

Industry/Entity Type

Voip

Requirements
Must have
• Feature and benefits information of Managed VOICE. Use my logo and coloring from my logo. Include our website, email, phone and possibly facebook if it makes sense/looks good.

www.lumenbyharlow-example.com
415.836.0.917
sales@lumenbyharlow-example.com
www.socialsite-example.com/lumenbyharlow
Nice to have
• Would like to show how the service is simple and reliable and available for any business size

```html
<!DOCTYPE html>
<html lang="en">
<head>
<meta charset="utf-8">
<title>IT Consulting &amp; Services</title>
<link rel="stylesheet" href="https://fonts.googleapis.com/css2?family=Roboto:ital,wght@0,700;0,900;1,900&family=Roboto+Condensed:wght@700&display=swap">
<style>
  :root {
    --brand-red: #8b1a1e;
    --brand-navy: #1b2d5a;
    --accent-blue: #2aa3e0;
    --text-gray: #58595b;
    --paper: #ffffff;
    --backdrop: #e6e7e8;
  }
  * { box-sizing: border-box; margin: 0; padding: 0; }
  html, body {
    width: 921px; height: 1200px; overflow: hidden;
    background: var(--backdrop);
  }
  .flyer {
    position: absolute; left: 36px; top: 0;
    width: 849px; height: 1200px;
    background: var(--paper);
    overflow: hidden;
    font-family: "Roboto", Arial, sans-serif;
  }
  .hero-visual {
    position: absolute; left: 0; top: 0; width: 849px; height: 526px;
    background:
      radial-gradient(ellipse 150px 130px at 630px 320px, rgba(200,240,255,.55), rgba(90,190,240,.25) 60%, transparent 100%),
      radial-gradient(ellipse 420px 300px at 640px 330px, rgba(70,170,225,.7), rgba(30,110,170,.4) 55%, transparent 85%),
      radial-gradient(ellipse 260px 200px at 800px 120px, rgba(60,140,200,.45), transparent 80%),
      linear-gradient(110deg, #141b26 0%, #1c2838 30%, #1f4263 60%, #1a3d5e 100%);
  }
  .title-banner {
    position: absolute; left: 0; top: 55px; width: 557px; height: 181px;
  }
  .title-banner svg { position: absolute; inset: 0; }
  .title-banner h1 {
    position: absolute; left: 30px; top: 18px;
    color: var(--paper);
    font-style: italic; font-weight: 900;
    font-size: 66px; line-height: 75px; letter-spacing: -.3px;
    white-space: nowrap;
  }
  .section-tab {
    position: absolute; left: 207px; top: 496px; width: 437px; height: 61px;
  }
  .section-tab svg { position: absolute; inset: 0; }
  .section-tab h2 {
    position: absolute; left: 25px; right: 27px; top: 0; height: 61px;
    display: flex; align-items: center; justify-content: center;
    color: var(--paper); font-weight: 900; font-size: 43px; letter-spacing: .3px;
  }
  .intro {
    position: absolute; left: 0; right: 0; top: 560px;
    text-align: center; color: var(--text-gray);
    font-weight: 700; font-size: 26px; line-height: 30px; letter-spacing: .2px;
  }
  .service-card {
    position: absolute; width: 237px; height: 209px;
  }
  .service-card::before {
    content: ""; position: absolute; left: 19px; top: 12px; width: 218px; height: 197px;
    border: 2px solid var(--brand-red);
  }
  .service-card .card-body {
    position: absolute; left: 0; top: 0; width: 218px; height: 195px;
    background: var(--brand-navy);
    padding: 28px 12px 0; text-align: center;
  }
  .service-card h3 {
    color: var(--accent-blue); font-weight: 700;
    font-size: 27px; line-height: 31px; letter-spacing: .3px;
    margin-bottom: 18px;
  }
  .service-card p {
    color: var(--paper);
    font-family: "Roboto Condensed", "Arial Narrow", sans-serif;
    font-weight: 700; font-size: 12.5px; line-height: 17px;
    padding: 0 4px;
  }
  .col-1 { left: 45px; } .col-2 { left: 308px; } .col-3 { left: 571px; }
  .row-1 { top: 636px; } .row-2 { top: 865px; }
  .footer-rule {
    position: absolute; left: 0; top: 1099px; width: 849px; height: 6px;
    background: var(--brand-navy);
  }
  .contact-footer {
    position: absolute; left: 0; top: 1105px; width: 849px; height: 95px;
    background: var(--brand-red);
    color: var(--paper); text-align: center;
    font-weight: 700; font-size: 21.5px; line-height: 33px;
    padding-top: 14px; white-space: nowrap;
  }
</style>
</head>
<body>
<div class="flyer">
  <div class="hero-visual" role="img" aria-label="Photo of a hand holding a glowing digital network with a padlock, cloud, server and lightbulb icons"></div>

  <div class="title-banner">
    <svg width="557" height="181" viewBox="0 0 557 181" aria-hidden="true">
      <path d="M0 0 H557 C525 95 475 165 380 181 H0 Z" fill="var(--brand-red)"/>
    </svg>
    <h1>IT CONSULTING<br>&amp; SERVICES</h1>
  </div>

  <div class="section-tab">
    <svg width="437" height="61" viewBox="0 0 437 61" aria-hidden="true">
      <path d="M0 33 H25 V61 Z" fill="var(--brand-navy)"/>
      <path d="M437 33 H410 V61 Z" fill="var(--brand-navy)"/>
      <rect x="25" y="0" width="385" height="61" fill="var(--brand-red)"/>
    </svg>
    <h2>OUR SERVICES</h2>
  </div>

  <p class="intro">We provide a complete range of IT services focused on<br>you getting the most from your technology.</p>

  <section class="service-card col-1 row-1"><div class="card-body">
    <h3>MANAGED IT SERVICES</h3>
    <p>You need your IT systems for your day to day work. Let us help manage and protect them.</p>
  </div></section>
  <section class="service-card col-2 row-1"><div class="card-body">
    <h3>Business VOIP Phone Service</h3>
    <p>Reduce cost and improve communication for your business. Solutions available for any size business from 1 phone to hundreds of phones.</p>
  </div></section>
  <section class="service-card col-3 row-1"><div class="card-body">
    <h3>HOME PHONE SERVICE</h3>
    <p>Tired of the high cost and limited features of your old provider? Let us help you move to a low cost full featured VOIP home phone solution.</p>
  </div></section>

  <section class="service-card col-1 row-2"><div class="card-body">
    <h3>NETWORK SECURITY</h3>
    <p>Worried about the latest ransomware or crypto virus? We can help design and protect your network.</p>
  </div></section>
  <section class="service-card col-2 row-2"><div class="card-body">
    <h3>WIRELESS SOLUTIONS</h3>
    <p>Is your wireless coverage spotty or would you like to extend your network or internet coverage to another building?</p>
  </div></section>
  <section class="service-card col-3 row-2"><div class="card-body">
    <h3>CLOUD SERVICES</h3>
    <p>Want your own business email service? Want to move to the cloud for secure file storage and sharing? Ask us about our complete cloud solution services.</p>
  </div></section>

  <div class="footer-rule"></div>
  <footer class="contact-footer">
    www.lumenbyharlow-example.com | 415.836.0.917<br>
    sales@lumenbyharlow-example.com | www.socialsite-example.com/lumenbyharlow
  </footer>
</div>
</body>
</html>
```